Casas de Nueva Aurora Flyer

Make me a flyer postcard 5 x 7 horizontal, one sided. I want main title to be "Casas de Nueva Aurora". It needs to say “Familias que se forman en la fe y valores humanos, y trabajan para llevar a otras familias al encuentro con Cristo y la Virgen María.”  We are in 4 places, include this:
Reuniones Cada Domingo
Los Olmos, Falls Church: 11:15am - 301-555-0142
Monte Claro, Sterling: 9:30am - 571-555-0187
Hogar Valle Sereno, 9:45am - 703-555-0163
Puerta Dorada, Winchester: 2:30pm - 540-555-0129
Include the logo attached, and use the picture attached as the main image, you can select the people from the image only and delete background or keep background but make it fit in nicely to the postcard.

```html
<!DOCTYPE html>
<html lang="es">
<head>
<meta charset="utf-8">
<title>Casas de Nueva Aurora – Postal</title>
<link href="https://fonts.googleapis.com/css2?family=Bebas+Neue&family=Great+Vibes&display=swap" rel="stylesheet">
<style>
  :root {
    --stage: #ececec;
    --brown: #33150f;
    --gold: #f2c23e;
    --white: #ffffff;
    --leaf: #4f7a3a;
    --sky: #b9cde0;
  }
  * { box-sizing: border-box; margin: 0; padding: 0; }
  html, body { width: 1200px; height: 918px; overflow: hidden; background: var(--stage); }
  .postcard {
    position: absolute; left: 20px; top: 44px;
    width: 1160px; height: 829px;
    background: var(--brown);
    overflow: hidden;
    font-family: "Bebas Neue", "Arial Narrow", sans-serif;
  }
  .group-photo {
    position: absolute; left: 0; top: 0; width: 1160px; height: 520px;
    background:
      linear-gradient(180deg, rgba(51,21,15,0) 58%, rgba(51,21,15,0.75) 80%, var(--brown) 100%),
      radial-gradient(ellipse at 60% 55%, #6d7fa8 0%, #8c6e74 35%, rgba(140,110,116,0) 65%),
      linear-gradient(180deg, var(--sky) 0%, var(--leaf) 22%, #5f7348 45%, #7a6257 70%, #6a4a3c 100%);
  }
  .brand-mark {
    position: absolute; left: 200px; top: 40px;
    display: flex; align-items: center; gap: 10px;
    color: var(--white); font-size: 26px; letter-spacing: 1px;
  }
  .brand-mark .square { width: 22px; height: 22px; background: var(--gold); }
  .mission {
    position: absolute; left: 140px; right: 140px; top: 268px;
    text-align: center; color: var(--white);
    font-size: 24px; line-height: 27px; letter-spacing: 0.5px;
    text-shadow: 0 1px 4px rgba(0,0,0,0.55);
  }
  .title {
    position: absolute; left: 0; right: 0; top: 330px;
    text-align: center; color: var(--white);
    font-size: 134px; line-height: 1; letter-spacing: 1px;
  }
  .subtitle {
    position: absolute; left: 0; right: 0; top: 458px;
    text-align: center; color: var(--white);
    font-family: "Great Vibes", cursive;
    font-size: 76px; line-height: 1;
  }
  .location {
    position: absolute; width: 430px;
    text-align: center; color: var(--gold);
    font-size: 40px; line-height: 48px;
  }
  .location.left { left: 96px; }
  .location.right { left: 624px; }
  .location.top { top: 567px; }
  .location.bottom { top: 702px; }
  .rule { position: absolute; top: 682px; height: 3px; width: 430px; background: var(--white); }
  .rule.left { left: 107px; }
  .rule.right { left: 625px; }
  .divider { position: absolute; left: 566px; top: 576px; width: 1px; height: 206px; background: var(--white); }
</style>
</head>
<body>
  <main class="postcard">
    <div class="group-photo" role="img" aria-label="Foto de grupo de las familias de la comunidad reunidas al aire libre en un parque"></div>

    <div class="brand-mark"><span class="square"></span>Casas de Nueva Aurora</div>

    <p class="mission">Familias que se forman en la fe y valores humanos, y trabajan para llevar a otras familias al encuentro con Cristo y la Virgen María.</p>

    <h1 class="title">CASAS DE NUEVA AURORA</h1>
    <p class="subtitle">Reuniones Cada Domingo</p>

    <p class="location left top">Los Olmos, Falls Church:<br>11:15AM - 301-555-0142</p>
    <p class="location right top">Monte Claro, Sterling:<br>9:30AM - 571-555-0187</p>

    <div class="rule left"></div>
    <div class="rule right"></div>
    <div class="divider"></div>

    <p class="location left bottom">Hogar Valle Sereno,<br>9:45AM - 703-555-0163</p>
    <p class="location right bottom">Puerta Dorada, Winchester:<br>2:30PM - 540-555-0129</p>
  </main>
</body>
</html>
```